Orsabellitravel.com web design project + logo design

Hi,

We are a Russian online tour operator - tripwelder.com

We are looking to tranmsfer our domain to orsabellitravel.com. The website and logo need to be orsabelliesque - we are not looking to change our functionality, but we need to make the website much more attracitve to clients, much more wild looking but at the same time remaining a professional travel company.

The main concept of the website should be innovative travel (as orsabelli was an innovator). Alternatively, you could go down the artist route and go down the draw / design your own tour road.

On our website the customer is able to combine travel services (hotels, flights, Visa services, and soon chauffeur, car rental etc...) put it into their basket (the basket definitely has to look better than it is at the moment) and pay for it in one go by card.

We are also stressin our customer support with web chat, call centre etc... (call centre number at the top of the page)

We aim to provide an easy user experience, but we need to make it have some more style, so I will be waiting for what you guys can come up with.
Let me know if you have any questions - skype is: mrkolbuzov

It Company

• It is quite a simple task - to take the existing website tripwelder.com and orsabellisize it to create orsabellitravel.com, the functionality of the website will remain the same and there are not many pages in the website. Homepage, Checkout step1, Checkout step 2 (you can view both of these if you select a service) and the generic pages for T&C''s, Privacy policy etc...

IMPORTANT UPDATE

We are also looking at how the search results will look in the designs, (please do a search on our website for hotel / flight)

```html
<!DOCTYPE html>
<html lang="ru">
<head>
<meta charset="utf-8">
<title>OrsabelliTravel</title>
<link rel="stylesheet" href="https://fonts.googleapis.com/css2?family=Open+Sans:wght@300;400;600;700&display=swap">
<style>
:root{
  --header:#2b2b2b;
  --ink:#333;
  --white:#fff;
  --field:#6b6b6b;
  --visa:#34474d;
  --visa-dark:#2a3a3f;
  --visa-row:#304247;
  --visa-line:#4d6268;
  --light:#dedede;
  --light2:#d6d6d6;
  --footer:#333;
  --footer-box:#111;
  --btn:#3a4f56;
  --btn-edge:#5fb6d4;
  --cal-head:#cfcfcf;
  --cal-body:#e9e9e9;
}
*{box-sizing:border-box;margin:0;padding:0}
html,body{width:1200px;height:2851px;overflow:hidden}
body{font-family:"Open Sans",Arial,sans-serif;color:var(--ink);background:var(--white);position:relative}
.abs{position:absolute}

/* header */
.site-header{position:absolute;left:0;top:0;width:1200px;height:109px;background:var(--header);color:#fff}
.brand{position:absolute;left:107px;top:34px;display:flex;align-items:center;gap:14px;font-size:34px;font-weight:400;letter-spacing:1px}
.brand .mark{width:36px;height:36px;border-radius:50%;background:#fff}
.nav{position:absolute;top:44px;font-size:14px;text-transform:uppercase;display:flex;align-items:center;gap:10px}
.nav .ico{width:20px;height:16px;background:#ddd;border-radius:2px}
.cart-btn{position:absolute;left:1038px;top:44px;background:#ddd;color:#333;font-size:12px;padding:4px 10px;text-transform:uppercase}

/* hero */
.hero{position:absolute;left:0;top:109px;width:1200px;height:592px;background:linear-gradient(180deg,#6f93b4 0%,#b7c1c4 22%,#8b6a3c 45%,#4c3a22 70%,#1f1f14 100%)}
.contact-box{position:absolute;left:102px;top:447px;width:371px;height:142px;background:rgba(42,58,66,.92);color:#fff;padding:22px 34px}
.contact-box .phone-main{font-size:38px;font-weight:700}
.contact-box .phone-alt{font-size:28px;font-weight:300;text-align:right}
.hours-box{position:absolute;left:102px;top:589px;width:371px;height:112px;background:rgba(20,20,20,.9);color:#fff;padding:14px 34px;font-size:26px;font-weight:300}
.hours-box .time{font-size:36px;text-align:right;line-height:1.2}
.slogan{position:absolute;left:473px;top:447px;width:596px;height:254px;background:rgba(52,72,80,.82);color:#fff;text-align:center;font-weight:400;line-height:1}
.slogan .l1{font-size:96px;margin-top:16px}
.slogan .l2{font-size:50px}
.slogan .l3{font-size:66px}
.pointer{position:absolute;left:422px;top:701px;width:0;height:0;border-left:18px solid transparent;border-right:18px solid transparent;border-top:18px solid #141414}

/* booking */
.tabs{position:absolute;left:116px;top:737px;width:960px;height:36px;border-bottom:2px solid #ddd;display:flex;font-size:22px}
.tab{padding:0 24px;line-height:36px}
.tab.active{background:#d6d6d6}
.label{position:absolute;font-size:17px;color:#444}
.field{position:absolute;height:38px;background:var(--field);color:#ddd;font-size:12px;line-height:38px;padding-left:14px}
.select{position:absolute;height:34px;background:var(--field);color:#ddd;font-size:11px;line-height:34px;padding-left:10px}
.select::after{content:"";position:absolute;right:0;top:0;width:26px;height:34px;background:#ccc}
.check{position:absolute;font-size:11px;display:flex;align-items:center;gap:5px;color:#444}
.check i{width:12px;height:12px;background:#555;display:block}
.search-btn{position:absolute;left:701px;top:934px;width:276px;height:92px;background:var(--btn);border:3px solid var(--btn-edge);color:#fff;font-size:40px;display:flex;align-items:center;justify-content:center;gap:6px}
.month{position:absolute;left:131px;top:1050px;font-size:26px}
.calendar{position:absolute;left:126px;top:1095px;width:969px;height:255px;display:grid;grid-template-columns:repeat(7,1fr);grid-template-rows:50px 1fr;background:var(--cal-body);border:1px solid #ccc}
.calendar .day{background:var(--cal-head);font-size:13px;color:#555;text-align:center;line-height:50px;border-right:1px solid #bbb}
.calendar .cell{border-right:1px solid #d0d0d0;margin:10px 0}

/* visa */
.visa{position:absolute;left:0;top:1390px;width:1200px;height:701px;background:var(--visa);color:#fff}
.section-title{position:absolute;display:flex;align-items:center;gap:14px;font-size:64px;font-weight:400}
.visa .sub{position:absolute;left:131px;top:84px;font-size:31px;font-weight:400}
.visa-table{position:absolute;left:112px;top:126px;width:957px;height:451px;background:var(--visa-dark);border:1px solid var(--visa-line);font-size:12px;line-height:1.45}
.row{position:absolute;left:0;width:100%;display:grid;grid-template-columns:1fr 1fr;gap:40px;padding:0 22px}
.row.full{display:block;text-align:center}
.row.shade{background:var(--visa-row)}
.dot{position:absolute;left:470px;width:16px;height:16px;border-radius:50%;background:#ccc}
.muted{color:#9aa}
.visa .note{position:absolute;left:126px;top:612px;font-size:20px}
.visa .countries{position:absolute;left:131px;top:640px;font-size:14px}

/* services */
.service{position:absolute;left:0;width:1200px;padding-left:131px}
.service h3{position:absolute;left:131px;font-size:30px;font-weight:400}
.service p{position:absolute;left:131px;width:950px;font-size:12px;line-height:1.5;color:#555}
.avia{top:2091px;height:268px;background:var(--light)}
.hotels{top:2359px;height:266px;background:var(--light2);border-top:4px solid #eee}

/* footer */
.site-footer{position:absolute;left:0;top:2625px;width:1200px;height:226px;background:var(--footer);color:#fff}
.fcol{position:absolute;top:40px;font-size:13px;line-height:1.3}
.fcol h4{font-size:17px;font-weight:400;margin-bottom:22px}
.fbox{position:absolute;left:551px;top:0;width:535px;height:226px;background:var(--footer-box)}
.fbrand{position:absolute;left:20px;top:36px;display:flex;align-items:center;gap:10px;font-size:28px}
.fbrand .mark{width:30px;height:30px;border-radius:50%;background:#fff}
.fline{position:absolute;left:30px;display:flex;align-items:center;gap:18px;font-size:13px}
.fline .c{width:24px;height:24px;border-radius:50%;border:2px solid #ccc;flex:none}
.social{position:absolute;top:165px;width:36px;height:36px;border-radius:50%;background:#fff}
</style>
</head>
<body>

<header class="site-header">
  <div class="brand"><span class="mark"></span>ORSABELLITRAVEL</div>
  <nav>
    <div class="nav" style="left:542px"><span class="ico"></span>Форум</div>
    <div class="nav" style="left:682px"><span class="ico"></span>Язык</div>
    <div class="nav" style="left:832px"><span class="ico"></span>Мой тур</div>
    <div class="nav" style="left:946px">
      <svg width="26" height="22" viewBox="0 0 26 22"><path d="M1 2h5l3 12h13l3-9H8" fill="none" stroke="#fff" stroke-width="2"/><circle cx="11" cy="19" r="2" fill="#fff"/><circle cx="20" cy="19" r="2" fill="#fff"/></svg>
    </div>
  </nav>
  <div class="cart-btn">Корзина (0) ▾</div>
</header>

<div class="hero" role="img" aria-label="Фотография заснеженных гор в лучах заката над зелёной долиной"></div>
<div class="contact-box">
  <div class="phone-main">8-800-555-0142</div>
  <div class="phone-alt">+7 (495) 555-01-27</div>
</div>
<div class="hours-box">
  <div>(Пн-Пт) Часы работы</div>
  <div class="time">с 9:00 - до 18:00</div>
</div>
<div class="slogan">
  <div class="l1">Больше</div>
  <div class="l2">чем опыт</div>
  <div class="l3">путешествия</div>
</div>
<div class="pointer"></div>

<section class="booking">
  <div class="tabs"><span class="tab active">Корзина</span><span class="tab" style="padding-left:48px">пусто</span><span class="tab">Оплата</span></div>

  <div class="label" style="left:131px;top:818px">Откуда</div>
  <div class="field" style="left:252px;top:808px;width:325px">Город</div>
  <div class="label" style="left:627px;top:818px">Куда</div>
  <div class="field" style="left:698px;top:808px;width:279px">Город</div>

  <div class="label" style="left:131px;top:879px">Туда</div>
  <div class="field" style="left:252px;top:869px;width:325px">&#9638;&nbsp;&nbsp;&nbsp;(16-6-2013)</div>
  <div class="label" style="left:627px;top:879px">Обратно</div>
  <div class="field" style="left:698px;top:869px;width:279px">(Обратно)</div>
  <div class="check" style="left:986px;top:870px"><i></i>Обратно</div>
  <div class="check" style="left:986px;top:891px"><i></i>В одну сторону</div>

  <div class="label" style="left:131px;top:934px">Пассажиры</div>
  <div class="select" style="left:252px;top:924px;width:88px;padding-left:30px">(1)</div>
  <div class="select" style="left:368px;top:924px;width:88px;padding-left:30px">(0)</div>
  <div class="select" style="left:489px;top:924px;width:88px;padding-left:30px">(0)</div>

  <div class="label" style="left:131px;top:1001px">Класс</div>
  <div class="select" style="left:252px;top:991px;width:328px">Эконом</div>

  <div class="search-btn">Поиск
    <svg width="36" height="36" viewBox="0 0 36 36"><circle cx="14" cy="14" r="10" fill="none" stroke="#fff" stroke-width="5"/><path d="M21 21l11 11" stroke="#fff" stroke-width="6"/></svg>
  </div>

  <div class="month">Янв</div>
  <div class="calendar">
    <div class="day">Чт, 01</div><div class="day">Пт, 02</div><div class="day">Сб, 03</div><div class="day">Вс, 04</div><div class="day">Пн, 05</div><div class="day">Вт, 0</div><div class="day">Ср, 07</div>
    <div class="cell"></div><div class="cell"></div><div class="cell"></div><div class="cell"></div><div class="cell"></div><div class="cell"></div><div class="cell"></div>
  </div>
</section>

<section class="visa">
  <div class="section-title" style="left:124px;top:8px">
    <svg width="46" height="58" viewBox="0 0 46 58"><rect x="6" y="3" width="36" height="52" rx="3" fill="none" stroke="#fff" stroke-width="4"/><path d="M2 14h8M2 28h8M2 42h8" stroke="#fff" stroke-width="4"/></svg>
    ВИЗЫ
  </div>
  <div class="sub">Возможны два варианта подачи на визу</div>
  <div class="visa-table">
    <div class="row" style="top:14px">
      <div>1.Оформление визы «Онлайн»<br><br>Вы сможете подать на визу, отправить и получить обратно свои документы «не выходя из дома»!</div>
      <div>2.Оформление визы «Самостоятельно».<br><br>С этой услугой требуется ваше присутствие в визовом центре. Услуга бесплатная, однако, нужно нажать на кнопку «Выбрать», а затем на «Оплата» (0 руб.)</div>
    </div>
    <div class="dot" style="top:90px"></div>
    <div class="row full shade" style="top:110px;padding:8px 22px">После бронирования выбранной услуги, необходимо заполнить простую форму на визовую анкету на только что созданной для вас личной странице.<br>Заполнение формы pdf-файл анкеты будет создан автоматически.</div>
    <div class="dot" style="top:172px"></div>
    <div class="row" style="top:196px">
      <div>Вам будет предоставлен ассистент, который в частном порядке проконсультирует вас по всем вопросам, касающимся заполнения анкет, оформления визы и т.д.<br>Контактная информация будет на вашей личной странице и будет выслана вам на электронную почту.</div>
      <div>По всем вопросам оформления виз, заполнения анкет, о месторасположении ближайшего визового центра и т.д. звоните в наш колл центр.<br>Часы работы колл центра: с 9:00 до 21:00 ежедневно. Здесь вы получите профессиональную консультацию.</div>
    </div>
    <div class="row full shade muted" style="top:300px;padding:8px 22px">После того, как вы пройдёте по предоставленному на сайте списку и убедитесь, что у вас есть все необходимые для подачи на визу документы</div>
    <div class="dot" style="top:346px"></div>
    <div class="row" style="top:372px">
      <div>мы отправим к вам курьера в удобное для вас время. Наш ассистент сообщит вам о готовности вашей визы и, согласовав с вами время курьером мы доставим вам паспорт</div>
      <div>вы направляетесь в визовый центр и самостоятельно, сначала подаете, а потом забираете уже оформленные документы.</div>
    </div>
  </div>
  <div class="note">* Услуга «Виза онлайн» предоставляет возможность оформления визы в следующие страны:</div>
  <div class="countries">Австрия, Бельгия, Греция, Германия, Нидерланды, Норвегия, Швейцария, Швеция.</div>
</section>

<section class="service avia">
  <div class="section-title" style="left:131px;top:30px;color:#333">
    <svg width="52" height="46" viewBox="0 0 52 46"><path d="M2 21h18L30 2h6l-6 19h14l5-7h3l-3 9 3 9h-3l-5-7H30l6 19h-6L20 25H2z" fill="#333"/></svg>
    АВИАБИЛЕТЫ
  </div>
  <h3 style="top:114px">Авиабилеты от ТрипВелдер.</h3>
  <p style="top:162px">На нашем сайте вы можете рассматривать предложения от разных авиалиний и приобрести авиабилеты согласно вашим пожеланиям и бюджету.<br>Планируйте даты отправлений и прибытий с в любые страны, заполнив необходимые ячейки, ТрипВелдер автоматически отобразит вашу программу в календаре.<br>С ТрипВелдер вы можете создать любой Тур, в том числе и кругосветный и оплатить все услуги Единым платежом.</p>
</section>

<section class="service hotels">
  <div class="section-title" style="left:124px;top:24px;color:#333">
    <svg width="56" height="48" viewBox="0 0 56 48"><path d="M3 4v42M3 34h50v12M53 34V24H22v10" stroke="#333" stroke-width="5" fill="none"/><circle cx="13" cy="24" r="6" fill="#333"/></svg>
    ОТЕЛИ
  </div>
  <h3 style="top:108px">Отели от ТрипВелдер.</h3>
  <p style="top:156px">На нашем сайте вы можете рассматривать предложения от разных авиалиний и приобрести авиабилеты согласно вашим пожеланиям и бюджету.<br>Планируйте даты отправлений и прибытий с в любые страны, заполнив необходимые ячейки, ТрипВелдер автоматически отобразит вашу программу в календаре.<br>С ТрипВелдер вы можете создать любой Тур, в том числе и кругосветный и оплатить все услуги Единым платежом.</p>
</section>

<footer class="site-footer">
  <div class="fcol" style="left:131px"><h4>Просмотр Сайта</h4>Домой<br>О нас<br>Форум<br>Контакты<br>Помощь</div>
  <div class="fcol" style="left:358px"><h4>Помощь</h4>Помощь<br>Правила<br>пользования<br>Политика<br>конфиденциал<br>ьности<br>Cookies</div>
  <div class="fbox">
    <div class="fbrand"><span class="mark"></span>ORSABELLITRAVEL</div>
    <div class="fline" style="top:92px"><span class="c"></span><span>12 Harbour Row,<br>London, E1 4QZ, UK</span></div>
    <div class="fline" style="top:146px"><span class="c"></span>+7 (495) 555-01-27</div>
    <div class="fline" style="top:188px"><span class="c"></span>info@tripwelder.com</div>
    <div class="social" style="left:384px"></div>
    <div class="social" style="left:428px"></div>
    <div class="social" style="left:472px"></div>
  </div>
</footer>

</body>
</html>
```